The name of my company is Tolmen Refacing LLC and I would like the sub text to say "Cabinet Refacing and Countertops". Have my name Dorian Tolmen, Owner / Sales, contact info: Cell: 360-555-0147 / Email: dorian.tolmen@quenmail.com

Simple, Clean, and Organized. With colors that will appeal to the eye.

Target Market(s)

Houses and Apartments

Industry/Entity Type

Cabinet Refacing

Contact Information for Business Card

Company name and sub text Dorian Tolmen - Owner / Sales, my cell phone number and email

Requirements
Must have
• Business name, my name / position, and my contact info
Nice to have
• Simple. Organized. Appealing to the eye

```html
<!DOCTYPE html>
<html lang="en">
<head>
<meta charset="utf-8">
<title>Tolmen Refacing LLC — Business Card</title>
<link rel="stylesheet" href="https://fonts.googleapis.com/css2?family=Jost:wght@300;400&family=Roboto:wght@500;700&display=swap">
<style>
  :root {
    --page-bg: #ffffff;
    --brand-blue: #3c6cc4;
    --brand-blue-deep: #2d5bb2;
    --brand-blue-soft: #5b86d2;
    --panel-light: #f3f5f8;
    --panel-line: #dfe5ee;
    --text-blue: #3a66c0;
    --text-white: #ffffff;
  }
  html, body {
    margin: 0;
    padding: 0;
    width: 1200px;
    height: 848px;
    overflow: hidden;
    background: var(--page-bg);
  }
  .stage {
    position: relative;
    width: 1200px;
    height: 848px;
  }
  .card {
    position: absolute;
    overflow: hidden;
    box-shadow: 2px 3px 6px rgba(0, 0, 0, 0.22);
  }
  .card--back { left: 164px; top: 127px; width: 466px; height: 265px; }
  .card--front { left: 604px; top: 418px; width: 463px; height: 266px; }

  .card__pattern {
    position: absolute;
    inset: 0;
    background: linear-gradient(160deg, var(--brand-blue-soft) 0%, var(--brand-blue) 45%, var(--brand-blue-deep) 100%);
  }
  .card__shapes {
    position: absolute;
    inset: 0;
  }

  /* Contact side */
  .identity {
    position: absolute;
    left: 17px;
    top: 62px;
    display: inline-block;
  }
  .card--back .company-name {
    margin: 0;
    font-family: "Jost", sans-serif;
    font-weight: 300;
    font-size: 22px;
    line-height: 28px;
    text-transform: uppercase;
    white-space: nowrap;
    color: var(--text-blue);
  }
  .person {
    margin: 0;
    text-align: right;
    font-family: "Jost", sans-serif;
    font-weight: 300;
    font-size: 14px;
    line-height: 18px;
    white-space: nowrap;
    color: var(--text-blue);
  }
  .person__name { font-weight: 400; }

  .contact {
    position: absolute;
    left: 21px;
    top: 144px;
    margin: 0;
    padding: 0;
    list-style: none;
    font-family: "Roboto", sans-serif;
    font-weight: 700;
    font-size: 14px;
    color: var(--text-white);
  }
  .contact__item {
    display: flex;
    align-items: center;
    height: 26px;
    white-space: nowrap;
  }
  .contact__icon {
    width: 13px;
    height: 13px;
    margin-right: 13px;
    fill: var(--text-white);
  }

  .mark {
    position: absolute;
    display: flex;
    align-items: center;
    gap: 6px;
    font-family: "Jost", sans-serif;
    font-weight: 400;
    text-transform: uppercase;
    white-space: nowrap;
  }
  .mark__square {
    display: block;
    width: 12px;
    height: 12px;
  }
  .card--back .mark {
    left: 348px;
    top: 148px;
    font-size: 18px;
    color: var(--text-blue);
  }
  .card--back .mark__square { background: var(--text-blue); }

  /* Company side */
  .front-stack {
    position: absolute;
    left: 0;
    top: 70px;
    width: 476px;
    text-align: center;
    color: var(--text-white);
  }
  .card--front .mark {
    position: static;
    justify-content: center;
    font-size: 24px;
    height: 40px;
  }
  .card--front .mark__square { background: var(--text-white); width: 14px; height: 14px; }
  .card--front .company-name {
    margin: 20px 0 0;
    font-family: "Jost", sans-serif;
    font-weight: 300;
    font-size: 23px;
    line-height: 28px;
    text-transform: uppercase;
    white-space: nowrap;
  }
  .tagline {
    margin: 8px 0 0;
    font-family: "Roboto", sans-serif;
    font-weight: 700;
    font-size: 12.5px;
    letter-spacing: 0.05em;
    text-transform: uppercase;
    white-space: nowrap;
  }
</style>
</head>
<body>
<main class="stage">

  <section class="card card--back" aria-label="Business card contact side">
    <div class="card__pattern" role="img" aria-label="Faint pattern of cabinet door panels in blue tones"></div>
    <svg class="card__shapes" width="466" height="265" viewBox="0 0 466 265" aria-hidden="true">
      <polygon points="0,18 235,18 252,40 466,40 466,204 366,204 264,140 0,140" fill="var(--panel-light)"/>
      <rect x="0" y="14" width="466" height="4" fill="var(--panel-line)"/>
      <polygon points="0,140 264,140 366,204 0,204" fill="var(--brand-blue)" opacity="0.9"/>
      <line x1="0" y1="209" x2="366" y2="209" stroke="var(--panel-light)" stroke-width="2"/>
    </svg>

    <div class="identity">
      <h1 class="company-name">Tolmen Refacing LLC</h1>
      <p class="person"><span class="person__name">Dorian Tolmen</span> · Owner / Sales</p>
    </div>

    <ul class="contact">
      <li class="contact__item">
        <svg class="contact__icon" viewBox="0 0 24 24" aria-hidden="true">
          <path d="M6.6 10.8a15.1 15.1 0 0 0 6.6 6.6l2.2-2.2a1 1 0 0 1 1-.25 11.4 11.4 0 0 0 3.6.57 1 1 0 0 1 1 1V20a1 1 0 0 1-1 1A17 17 0 0 1 3 4a1 1 0 0 1 1-1h3.5a1 1 0 0 1 1 1c0 1.25.2 2.45.57 3.57a1 1 0 0 1-.25 1z"/>
        </svg>
        <span>360-555-0147</span>
      </li>
      <li class="contact__item">
        <svg class="contact__icon" viewBox="0 0 24 24" aria-hidden="true">
          <path d="M2 5h20v14H2z M3.5 6.5 12 13l8.5-6.5" fill="var(--text-white)" stroke="var(--brand-blue)" stroke-width="1.6"/>
        </svg>
        <span>dorian.tolmen@quenmail.com</span>
      </li>
    </ul>

    <div class="mark"><span class="mark__square"></span><span>Tolmen</span></div>
  </section>

  <section class="card card--front" aria-label="Business card company side">
    <div class="card__pattern" role="img" aria-label="Faint pattern of cabinet door panels in blue tones"></div>
    <div class="front-stack">
      <div class="mark"><span class="mark__square"></span><span>Tolmen</span></div>
      <h2 class="company-name">Tolmen Refacing LLC</h2>
      <p class="tagline">Cabinet Refacing &amp; Countertops</p>
    </div>
  </section>

</main>
</body>
</html>
```